President
General Contractor
I need single sided standard sized Business Card [3.5" x 2"]
I am open to ideas
Simple
Darnell Whitby
President/CEO
P.O. Box 7413
Orangeburg, South Carolina 29116
darnell@keystrelbuilderssc.example
www.keystrelbuilderssc.example
K573841 and R408657
Designers, you may want to check out my website. wwwkeystrelbuilderssc.example I have a log that Iam not crazy about. I want it to reflect more about residential and commerical construction, development and construction management.
I am open to using the back of the card.
Company's Logo

```html
<!DOCTYPE html>
<html lang="en">
<head>
<meta charset="utf-8">
<title>Keystrel Builders Stationery</title>
<link href="https://fonts.googleapis.com/css2?family=Roboto+Condensed:wght@400;700&family=Roboto:wght@400&display=swap" rel="stylesheet">
<style>
  :root {
    --maroon: #7b2c30;
    --maroon-dark: #5e1f23;
    --grey: #8d8d8d;
    --grey-light: #c9c9c9;
    --paper: #ffffff;
    --ink: #4a4a4a;
    --backdrop-a: #a4a4a4;
    --backdrop-b: #8a8a8a;
  }
  * { box-sizing: border-box; margin: 0; padding: 0; }
  html, body { width: 1200px; height: 626px; overflow: hidden; }
  body {
    position: relative;
    background: radial-gradient(ellipse at 50% 45%, var(--backdrop-a), var(--backdrop-b));
    font-family: "Roboto", Arial, sans-serif;
    color: var(--ink);
  }
  .sheet {
    position: absolute;
    background: var(--paper);
    overflow: hidden;
    box-shadow: 0 2px 6px rgba(0,0,0,.3);
  }
  .sheet svg.trim { position: absolute; inset: 0; width: 100%; height: 100%; }
  .brand {
    position: absolute;
    display: flex;
    align-items: center;
    gap: 5px;
    font-family: "Roboto Condensed", Arial, sans-serif;
    font-weight: 700;
    color: var(--maroon);
    text-transform: uppercase;
    line-height: 1;
  }
  .brand .mark { background: var(--maroon); flex: none; }
  .contact {
    position: absolute;
    font-size: 4.6px;
    line-height: 1.5;
    color: var(--ink);
  }

  /* Business card front */
  .card-front { left: 34px; top: 199px; width: 153px; height: 84px; }
  .card-front .brand { left: 30px; top: 35px; font-size: 11px; }
  .card-front .mark { width: 10px; height: 10px; }

  /* Business card back */
  .card-back { left: 34px; top: 307px; width: 153px; height: 89px; }
  .card-back .holder { position: absolute; right: 40px; top: 14px; text-align: right; font-size: 5px; line-height: 1.4; }
  .card-back .holder strong { font-family: "Roboto Condensed", Arial, sans-serif; font-size: 6px; color: var(--maroon); }
  .card-back .contact { left: 8px; top: 52px; font-size: 3.8px; }

  /* Letterhead */
  .letterhead { left: 233px; top: 31px; width: 362px; height: 564px; }
  .letterhead .brand { left: 26px; top: 26px; font-size: 11px; }
  .letterhead .mark { width: 12px; height: 12px; }
  .letterhead .watermark {
    position: absolute; left: 40px; top: 258px;
    font-family: "Roboto Condensed", Arial, sans-serif; font-weight: 700;
    font-size: 58px; color: #f3efef; text-transform: uppercase; letter-spacing: 1px;
  }
  .letterhead .contact { left: 26px; top: 520px; }

  /* DL envelope, back */
  .envelope-back { left: 679px; top: 79px; width: 487px; height: 190px; }

  /* DL envelope, front */
  .envelope-front { left: 679px; top: 336px; width: 487px; height: 221px; }
  .envelope-front .brand { left: 16px; top: 16px; font-size: 11px; }
  .envelope-front .mark { width: 12px; height: 12px; }
  .envelope-front .contact { left: 214px; top: 110px; }
</style>
</head>
<body>

  <section class="sheet card-front" aria-label="Business card front">
    <div class="brand"><span class="mark"></span>Keystrel Builders</div>
  </section>

  <section class="sheet card-back" aria-label="Business card back">
    <svg class="trim" viewBox="0 0 153 89" preserveAspectRatio="none" aria-hidden="true">
      <path d="M118 89 C128 70 126 40 138 22 C128 48 140 76 153 84 L153 89Z" fill="var(--grey)"/>
      <path d="M126 0 C140 28 128 62 146 89 L153 89 L153 0Z" fill="var(--maroon)"/>
    </svg>
    <div class="holder"><strong>Darnell Whitby</strong><br>President/CEO</div>
    <div class="contact">
      T: 803.555.0142<br>
      P.O. Box 7413, Orangeburg, SC 29116<br>
      darnell@keystrelbuilderssc.example<br>
      www.keystrelbuilderssc.example
    </div>
  </section>

  <section class="sheet letterhead" aria-label="Letterhead">
    <svg class="trim" viewBox="0 0 362 564" preserveAspectRatio="none" aria-hidden="true">
      <path d="M286 564 C326 480 318 410 330 330 C334 440 346 510 362 544 L362 564Z" fill="var(--grey)"/>
      <path d="M330 0 C346 160 318 380 344 564 L362 564 L362 0Z" fill="var(--maroon)"/>
    </svg>
    <div class="brand"><span class="mark"></span>Keystrel<br>Builders</div>
    <div class="watermark">Keystrel</div>
    <div class="contact">
      T: 803.555.0142<br>
      F: 803.555.0198<br>
      P.O. Box 7413, Orangeburg, South Carolina 29116<br>
      darnell@keystrelbuilderssc.example<br>
      www.keystrelbuilderssc.example
    </div>
  </section>

  <section class="sheet envelope-back" aria-label="Envelope back">
    <svg class="trim" viewBox="0 0 487 190" preserveAspectRatio="none" aria-hidden="true">
      <path d="M0 0 L487 0 L487 30 L0 30Z" fill="var(--maroon)"/>
      <path d="M0 30 L487 30" stroke="var(--maroon-dark)" stroke-width="1"/>
      <path d="M440 190 C470 150 462 90 478 30 L487 30 L487 190Z" fill="var(--maroon)"/>
    </svg>
  </section>

  <section class="sheet envelope-front" aria-label="Envelope front">
    <svg class="trim" viewBox="0 0 487 221" preserveAspectRatio="none" aria-hidden="true">
      <path d="M400 221 C440 190 450 150 470 110 C466 160 476 195 487 205 L487 221Z" fill="var(--grey)"/>
      <path d="M430 221 C468 180 470 110 487 60 L487 221Z" fill="var(--maroon)"/>
    </svg>
    <div class="brand"><span class="mark"></span>Keystrel<br>Builders</div>
    <div class="contact">
      T: 803.555.0142<br>
      F: 803.555.0198<br>
      P.O. Box 7413, Orangeburg, South Carolina 29116<br>
      darnell@keystrelbuilderssc.example<br>
      www.keystrelbuilderssc.example
    </div>
  </section>

</body>
</html>
```